New Business Card Design Project VORASTI-Italy

we are VORASTI-Italy
our company in the market for 3 years we are luxury cosmetic company and its about time for a facelift :)
i will like to have elegant luxurious and unique business card
that will give the person that get it a unique, luxurious and elegant impression
I'm VERY OPEN FOR NEW IDEAS , even duo i add a few files of things that i see on line and i like them

i add my logo as well
my website is VORASTI.COM
(if you would like to see the main style that we have)

Target Market(s)

adult that have money :)

Industry/Entity Type

Business

Contact Information for Business Card

Name - Paul Vorasti
Position - CEO and CO Founder
address - 4817 E Larkdale
telephone - 555-384-1962
email - paul@vorasti.com
fax - 555-384-1962
website - VORASTI.COM

Colors
000000
959595
fbee3e
ffffff

Requirements
Must have
• big logo in GOLD color
• elegant look
• impressive
Nice to have
• not must but maybe classy pattern background
• not must but maybe emblem
• maybe clear plastic business card
Should not have
• colors
• images

```html
<!DOCTYPE html>
<html lang="en">
<head>
<meta charset="utf-8">
<title>VORASTI Italy – Business Card</title>
<link rel="stylesheet" href="https://fonts.googleapis.com/css2?family=Cinzel:wght@500&family=Arimo:wght@400;700&display=swap">
<style>
  :root {
    --stage: #2b2d31;
    --card-black: #050505;
    --gold: #c9a233;
    --yellow: #f7ec3e;
    --grey: #959595;
    --ink: #000000;
    --white: #ffffff;
  }
  * { box-sizing: border-box; margin: 0; padding: 0; }
  html, body { width: 1200px; height: 900px; overflow: hidden; }
  body {
    background: var(--stage);
    font-family: "Arimo", Arial, sans-serif;
    position: relative;
  }
  .card {
    position: absolute;
    width: 560px;
    height: 320px;
    border-radius: 26px;
    overflow: hidden;
    box-shadow: 0 18px 40px rgba(0,0,0,0.45);
  }
  .card--front { left: 320px; top: 70px; background: var(--card-black); }
  .card--back { left: 320px; top: 500px; background: var(--yellow); }

  .brand {
    position: absolute;
    display: flex;
    align-items: center;
    gap: 16px;
    color: var(--gold);
    font-family: "Cinzel", "Times New Roman", serif;
    font-weight: 500;
    white-space: nowrap;
  }
  .brand__dot {
    width: 22px; height: 22px;
    border-radius: 50%;
    background: var(--gold);
    flex: none;
  }
  .card--front .brand {
    left: 50%; top: 118px;
    transform: translateX(-50%);
    font-size: 46px;
    letter-spacing: 2px;
  }
  .front__rule {
    position: absolute;
    left: 0; right: 0; bottom: 34px;
    height: 3px;
    background: var(--yellow);
  }

  .back__shape { position: absolute; inset: 0; width: 100%; height: 100%; }
  .card--back .brand {
    left: 34px; top: 142px;
    font-size: 32px;
    letter-spacing: 1px;
  }
  .card--back .brand__dot { width: 16px; height: 16px; }

  .contact {
    position: absolute;
    left: 330px; top: 34px;
    color: var(--ink);
  }
  .contact__name { font-weight: 700; font-size: 19px; }
  .contact__role { font-weight: 700; font-size: 12px; margin-top: 2px; }
  .contact__address { font-weight: 700; font-size: 12px; margin-top: 26px; }
  .contact__list { list-style: none; margin-top: 22px; }
  .contact__item {
    display: flex; align-items: center; gap: 10px;
    font-weight: 700; font-size: 13px;
    margin-bottom: 8px;
  }
  .contact__icon { width: 28px; height: 28px; flex: none; }
</style>
</head>
<body>

  <section class="card card--front" aria-label="Card front">
    <div class="brand"><span class="brand__dot"></span><span class="brand__name">VORASTI ITALY</span></div>
    <div class="front__rule"></div>
  </section>

  <section class="card card--back" aria-label="Card back">
    <svg class="back__shape" viewBox="0 0 560 320" preserveAspectRatio="none" aria-hidden="true">
      <path d="M0 0 H270 C330 80 335 230 300 320 H0 Z" fill="#959595"/>
      <path d="M0 0 H260 C318 80 322 230 288 320 H0 Z" fill="#050505"/>
    </svg>
    <div class="brand"><span class="brand__dot"></span><span class="brand__name">VORASTI ITALY</span></div>

    <div class="contact">
      <p class="contact__name">Paul Vorasti</p>
      <p class="contact__role">CEO and CO Founder</p>
      <p class="contact__address">4817 E Larkdale</p>
      <ul class="contact__list">
        <li class="contact__item">
          <svg class="contact__icon" viewBox="0 0 28 28" aria-label="Phone"><circle cx="14" cy="14" r="12.5" fill="none" stroke="#000" stroke-width="1.8"/><path d="M9 8 l3 -1 l2 4 l-2 1.5 c1 2 2.5 3.5 4.5 4.5 l1.5 -2 l4 2 l-1 3 c-6 1 -13 -6 -12 -12 z" fill="#000"/></svg>
          <span>555-384-1962</span>
        </li>
        <li class="contact__item">
          <svg class="contact__icon" viewBox="0 0 28 28" aria-label="Fax"><circle cx="14" cy="14" r="12.5" fill="none" stroke="#000" stroke-width="1.8"/><rect x="10" y="7" width="8" height="5" fill="#000"/><rect x="7" y="11" width="14" height="7" rx="1" fill="#000"/><rect x="10" y="16" width="8" height="5" fill="#000" stroke="#f7ec3e" stroke-width="1"/></svg>
          <span>555-384-1962</span>
        </li>
        <li class="contact__item">
          <svg class="contact__icon" viewBox="0 0 28 28" aria-label="Email"><circle cx="14" cy="14" r="12.5" fill="none" stroke="#000" stroke-width="1.8"/><rect x="7" y="9" width="14" height="10" fill="#000"/><path d="M7 9 l7 6 l7 -6" fill="none" stroke="#f7ec3e" stroke-width="1.2"/></svg>
          <span>paul@vorasti.com</span>
        </li>
        <li class="contact__item">
          <svg class="contact__icon" viewBox="0 0 28 28" aria-label="Website"><circle cx="14" cy="14" r="12.5" fill="none" stroke="#000" stroke-width="1.8"/><circle cx="14" cy="14" r="7.5" fill="none" stroke="#000" stroke-width="1.5"/><ellipse cx="14" cy="14" rx="3.5" ry="7.5" fill="none" stroke="#000" stroke-width="1.3"/><path d="M6.5 14 h15 M8 10 h12 M8 18 h12" stroke="#000" stroke-width="1.2"/></svg>
          <span>VORASTI.COM</span>
        </li>
      </ul>
    </div>
  </section>

</body>
</html>
```